Up to the Challenge? Canadian based consulting company needs a two sided business card design

A Canadian based security risk management consulting company needs a two-sided business card design. What we do is provide advice and guidance related to emergency, security and business continuity management for small, medium and large companies to help ensure the protection of their people, assets, information, services, operations and reputation.

The final design should be simple, only one or two colours, eye catching, professional and one that makes people look at three or more times just because it looks so darn good.

I have include examples of business cards I like.

Target Market(s)

Small, medium and large companies.

Industry/Entity Type

Security

Contact Information for Business Card

Business Card Size: Standard size of 3.5" (89mm) x 2.0" (51mm) - (see full specifications and guides on PRINTLY's website if required)
Card Stock: Looking to use PRINTLY's Velm 32pt stock textured paper - seam colour either chili red or black
Business Name: The Harrowgate Partners
Website: www.theharrowgatepartners.example
Telephone: (555)310-2968
Name: Dana Ostrander
Position: Principle
e-mail: Dana.Ostrander@theharrowgatepartners.example

Font styles to use
Serif

Colors
ec1f27
000000
9d9d9d
aaaaaa
606060

Requirements
Must have
• - "The Harrowgate Partners" logo (see uploaded files). I have included grey scale and colour versions.
• - Business card details (as above)
Nice to have
• - One side black or grey scale.
• - Other side would likely be white.
• - Everyone likes the silver logo on the black background.
• - Small element of colour i.e. red but I'm leaning more to greyscale.
Should not have
• - A lot of colour. Keep it simple.

```html
<!DOCTYPE html>
<html lang="en">
<head>
<meta charset="utf-8">
<title>The Harrowgate Partners — Business Card</title>
<link href="https://fonts.googleapis.com/css2?family=Cinzel:wght@400&family=Montserrat:wght@300;400&display=swap" rel="stylesheet">
<style>
  :root {
    --page-bg: #e9e8e6;
    --card-white: #f7f7f6;
    --card-grey: #545557;
    --ink-dark: #3a3a3a;
    --ink-mid: #606060;
    --accent-red: #ec1f27;
    --rule-grey: #606060;
    --emboss-grey: #747577;
  }
  * { margin: 0; padding: 0; box-sizing: border-box; }
  html, body { width: 1200px; height: 843px; overflow: hidden; background: var(--page-bg); }
  .canvas { position: relative; width: 1200px; height: 843px; }

  .card {
    position: absolute;
    top: 252px;
    width: 559px;
    height: 319px;
    border-radius: 15px;
    box-shadow: 0 3px 8px rgba(0,0,0,0.25);
    overflow: hidden;
  }
  .card--front { left: 28px; background: var(--card-white); }
  .card--back { left: 614px; background: var(--card-grey); }

  .person { position: absolute; left: 28px; top: 112px; border-left: 2px solid var(--accent-red); padding-left: 7px; }
  .person__name {
    font-family: "Cinzel", serif;
    font-size: 18px;
    letter-spacing: 0.5px;
    color: var(--ink-dark);
    line-height: 22px;
  }
  .person__role {
    font-family: "Montserrat", sans-serif;
    font-weight: 300;
    font-size: 14px;
    color: var(--ink-mid);
    line-height: 18px;
  }

  .contact { position: absolute; left: 29px; top: 157px; border-left: 1px solid var(--rule-grey); padding-left: 7px; list-style: none; }
  .contact__item {
    display: flex; align-items: center; gap: 8px;
    font-family: "Montserrat", sans-serif;
    font-weight: 300;
    font-size: 14px;
    color: var(--ink-dark);
    line-height: 17.5px;
  }
  .contact__icon { width: 10px; height: 10px; flex: none; }

  .brand { position: absolute; left: 0; right: 0; top: 108px; margin-left: 250px; text-align: center; width: 300px; }
  .brand__mark { width: 34px; height: 34px; background: var(--emboss-grey); margin: 0 auto 18px; }
  .brand__name {
    font-family: "Cinzel", serif;
    font-weight: 400;
    font-size: 22px;
    letter-spacing: 1px;
    line-height: 26px;
    color: var(--emboss-grey);
  }
</style>
</head>
<body>
<main class="canvas">
  <section class="card card--front" aria-label="Card front">
    <div class="person">
      <p class="person__name">DANA OSTRANDER</p>
      <p class="person__role">Principle</p>
    </div>
    <ul class="contact">
      <li class="contact__item">
        <svg class="contact__icon" viewBox="0 0 10 10" aria-hidden="true"><path d="M2 0.5 L3.8 2.6 L2.9 3.6 Q4 6 6.4 7.1 L7.4 6.2 L9.5 8 L8.3 9.5 Q1 8 0.5 1.7 Z" fill="#ec1f27"/></svg>
        <span>(555) 310-2968</span>
      </li>
      <li class="contact__item">
        <svg class="contact__icon" viewBox="0 0 10 10" aria-hidden="true"><rect x="0.5" y="2" width="9" height="6.5" fill="#ec1f27"/><path d="M0.5 2 L5 5.6 L9.5 2" fill="none" stroke="#f7f7f6" stroke-width="0.9"/></svg>
        <span>Dana.Ostrander@theharrowgatepartners.example</span>
      </li>
      <li class="contact__item">
        <svg class="contact__icon" viewBox="0 0 10 10" aria-hidden="true"><circle cx="5" cy="5" r="4.4" fill="none" stroke="#ec1f27" stroke-width="1.1"/><path d="M0.6 5 H9.4 M5 0.6 Q2 5 5 9.4 M5 0.6 Q8 5 5 9.4" fill="none" stroke="#ec1f27" stroke-width="0.8"/></svg>
        <span>www.theharrowgatepartners.example</span>
      </li>
    </ul>
  </section>

  <section class="card card--back" aria-label="Card back">
    <div class="brand">
      <div class="brand__mark" aria-hidden="true"></div>
      <p class="brand__name">THE HARROWGATE<br>PARTNERS</p>
    </div>
  </section>
</main>
</body>
</html>
```